Dental Office Needs- Flyer Design for Same Day Crowns

We need a flyer that will explain the benefits of the same day crown from the patient prospective. Not show pictures of the machine that makes the crowns. See attached material for content. The flyer should use the practices PMS colors of Green 562 and Blue 3025. The ad should say to the patient - I want to go this office and get my crown done there.
Updates

Project Deadline Extended Reason: The difference in the time zone between USA and Europe has caused issues. Minor changes still need to be worked out. Added Thursday, July 14, 2016

Target Market(s)

Dental Patients

Industry/Entity Type

Dental

Requirements
Must have
• Call to Action
• Business Address and Business Logo
• Classic Design
• images of a Happy 50 year old Couple
• Gives the benefits of the same day crown
Should not have
• No Images of tooth figures
• No before or after pictures

```html
<!DOCTYPE html>
<html lang="en">
<head>
<meta charset="utf-8">
<title>Harbor Lane Dental – Same-Day Digital Restorations Flyer</title>
<link rel="stylesheet" href="https://fonts.googleapis.com/css2?family=Open+Sans:ital,wght@0,400;0,600;0,700;1,600;1,700&display=swap">
<style>
  :root {
    --backdrop: #e4e4e4;
    --blue-deep: #0f4f78;
    --blue-mid: #2a6f98;
    --blue-light: #6fa3c4;
    --blue-text: #1b5f8c;
    --green: #00876a;
    --green-dark: #00684f;
    --paper: #ffffff;
    --sky-pale: #d9e9f3;
    --ink: #1e2a35;
  }
  * { box-sizing: border-box; margin: 0; padding: 0; }
  html, body { width: 1200px; height: 900px; overflow: hidden; }
  body {
    background: var(--backdrop);
    font-family: "Open Sans", Arial, sans-serif;
  }
  .flyer {
    position: absolute;
    left: 300px; top: 26px;
    width: 600px; height: 848px;
    background: var(--paper);
    overflow: hidden;
    box-shadow: 0 6px 20px rgba(0,0,0,.18);
  }
  .hero {
    position: absolute; left: 0; top: 0; width: 600px; height: 430px;
    background: linear-gradient(180deg, var(--blue-deep) 0%, var(--blue-mid) 45%, var(--blue-light) 78%, var(--sky-pale) 100%);
  }
  .hero-swoosh { position: absolute; left: 0; top: 0; }
  .headline {
    position: absolute; right: 20px; top: 38px; width: 570px;
    color: #fff; font-weight: 700; font-size: 23px; line-height: 1.25;
    text-transform: uppercase; text-align: right;
  }
  .goodbye-list { position: absolute; left: 0; top: 150px; list-style: none; }
  .goodbye-list li {
    width: 300px; height: 32px; margin-bottom: 6px;
    background: linear-gradient(90deg, var(--green) 0%, var(--green-dark) 100%);
    color: #fff; font-size: 12.5px; font-weight: 600; text-transform: uppercase;
    line-height: 32px; padding-left: 34px;
    border-bottom: 2px solid rgba(255,255,255,.35);
  }
  .intro {
    position: absolute; left: 318px; top: 156px; width: 262px;
    color: #fff; font-size: 10.5px; line-height: 1.4;
  }
  .intro p + p { margin-top: 7px; }
  .benefit-lead {
    position: absolute; left: 18px; top: 306px; width: 570px;
    color: var(--blue-deep); font-size: 12.5px; font-weight: 700; font-style: italic;
  }
  .benefit-list {
    position: absolute; left: 34px; top: 334px; list-style: none;
    color: var(--blue-deep); font-size: 11px; font-weight: 600; line-height: 1.55;
  }
  .case-photos { position: absolute; left: 222px; top: 330px; display: flex; gap: 8px; }
  .case-photo {
    width: 100px; height: 52px; border: 3px solid #fff;
    box-shadow: 0 1px 4px rgba(0,0,0,.25);
  }
  .case-photo.before { background: linear-gradient(90deg, #6b3f34, #8a6c62, #5b4a48); }
  .case-photo.after { background: linear-gradient(90deg, #8a4c40, #d6b9a3, #9a5a4c); }
  .divider { position: absolute; left: 0; top: 418px; width: 600px; height: 3px; background: var(--blue-deep); }
  .lower {
    position: absolute; left: 0; top: 421px; width: 600px; height: 400px;
    background: linear-gradient(180deg, #fff 0%, #f3f8fb 60%, #fff 100%);
  }
  .section-title {
    position: absolute; left: 40px; top: 440px;
    color: var(--blue-text); font-size: 19px; font-weight: 700; text-transform: uppercase;
  }
  .body-copy {
    position: absolute; left: 40px; top: 478px; width: 292px;
    color: var(--blue-text); font-size: 9.8px; line-height: 1.4;
    text-align: justify;
  }
  .body-copy p + p { margin-top: 9px; }
  .cta-line {
    position: absolute; left: 40px; top: 632px; width: 310px;
    color: var(--blue-text); font-size: 13.5px; font-weight: 600;
  }
  .couple-photo {
    position: absolute; left: 352px; top: 495px; width: 248px; height: 275px;
    background: linear-gradient(180deg, #cfe2ef 0%, #e8eef2 35%, #9fb8cc 70%, #f4f7f9 100%);
    border-top-left-radius: 120px 50px;
  }
  .brand { position: absolute; left: 40px; top: 700px; }
  .brand-name { display: flex; align-items: center; gap: 10px; color: var(--blue-text); font-size: 24px; font-weight: 400; }
  .brand-dot { width: 14px; height: 14px; border-radius: 50%; background: var(--green); }
  .brand-tagline { margin-top: 6px; color: var(--green); font-size: 12px; font-weight: 600; }
  .contact {
    position: absolute; right: 30px; top: 782px; text-align: right;
    color: var(--ink); font-size: 10.5px; line-height: 1.5; font-style: normal;
  }
  .footer-bar { position: absolute; left: 0; bottom: 0; width: 600px; height: 12px; background: var(--green); }
  .footer-rule { position: absolute; left: 0; bottom: 16px; width: 600px; height: 2px; background: var(--green); opacity: .5; }
</style>
</head>
<body>
  <main class="flyer">
    <section class="hero">
      <svg class="hero-swoosh" width="600" height="430" viewBox="0 0 600 430" aria-hidden="true">
        <path d="M0 150 C200 80 420 90 600 40 L600 0 L0 0 Z" fill="rgba(255,255,255,.06)"/>
        <path d="M0 300 C180 250 420 260 600 330" stroke="rgba(255,255,255,.25)" stroke-width="2" fill="none"/>
        <path d="M0 130 C220 100 430 130 600 115" stroke="rgba(255,255,255,.18)" stroke-width="1.5" fill="none"/>
      </svg>
      <h1 class="headline">Are you ready for a dramatically improved experience with your next crown?</h1>
      <ul class="goodbye-list">
        <li>Good-bye temporary crown</li>
        <li>Good-bye second appointment</li>
        <li>Good-bye gooey messy impressions</li>
      </ul>
      <div class="intro">
        <p>Harbor Lane Dental is pleased to offer you the Comfort and Convenience of One Visit Dental Care.</p>
        <p>We understand how hard it can be to take off work or have someone take care of the kids even once, but twice??</p>
        <p>Now with 3D CADCAM Technology, we can digitally design and mill a Customized, Ceramic Restoration in one appointment.</p>
      </div>
      <p class="benefit-lead">When it comes to your next crown, the benefits of a Digital Restoration add up quickly!</p>
      <ul class="benefit-list">
        <li>A Same-Day Restoration</li>
        <li>A Stronger More Precise Fit</li>
        <li>A Beautiful Natural Appearance</li>
      </ul>
      <div class="case-photos">
        <div class="case-photo before" role="img" aria-label="Close-up photo of a tooth with an old metal filling"></div>
        <div class="case-photo after" role="img" aria-label="Close-up photo of the same tooth with a ceramic restoration"></div>
      </div>
    </section>
    <div class="divider"></div>
    <section class="lower"></section>
    <h2 class="section-title">Same-Day Digital Restorations.</h2>
    <div class="body-copy">
      <p>Crowns, veneers and bridges that happen in hours instead of days. Ask your dentist if digital dentistry is right for you.</p>
      <p>Restorative dentistry has evolved and now, digital technology allows us to take an impression of your teeth with a digital scanner and create your restoration right in our office. We can match your existing teeth and provide you with a filling, veneer, crown or bridge using the most advanced non-metal composite materials giving you a beautiful smile and natural appearance.</p>
    </div>
    <p class="cta-line">Find out if digital dentistry is right for you.</p>
    <div class="couple-photo" role="img" aria-label="Photo of a smiling older couple walking arm in arm on a sunny beach"></div>
    <div class="brand">
      <div class="brand-name"><span class="brand-dot"></span>Harbor Lane Dental</div>
      <p class="brand-tagline">It All Begins With a Healthy Smile!</p>
    </div>
    <address class="contact">
      Company Address<br>
      Call to Action | +0123 456789
    </address>
    <div class="footer-rule"></div>
    <div class="footer-bar"></div>
  </main>
</body>
</html>
```